Teachers workshop flyer

I need a flyer to inform schools of a workshop for teachers that empowers the teacher to help traumatised and disadvantaged students to engage in successful learning.

I am a teacher and educator and my info for the flyer is attached.

Target Market(s)

Principals and vice-principals who have stressed staff and students and they want things to be better in the school!

Industry/Entity Type

Teacher

```html
<!DOCTYPE html>
<html lang="en">
<head>
<meta charset="utf-8">
<title>Brain-based Strategies for Student Success</title>
<link href="https://fonts.googleapis.com/css2?family=Oswald:wght@400;500&family=Crimson+Pro:ital,wght@0,400;0,700;1,300&display=swap" rel="stylesheet">
<style>
  :root {
    --orange: #f7a21b;
    --band: #f6a82a;
    --band-edge: #a8650f;
    --ink: #111111;
    --quote: #7a7a7a;
    --white: #ffffff;
  }
  * { margin: 0; padding: 0; box-sizing: border-box; }
  html, body { width: 845px; height: 1200px; overflow: hidden; background: var(--white); }
  .flyer { position: relative; width: 845px; height: 1200px; overflow: hidden; background: var(--white); }

  .title {
    position: absolute; left: 0; right: 0; top: 14px;
    text-align: center; color: var(--orange);
    font-family: "Oswald", sans-serif; font-weight: 500;
    font-size: 92px; line-height: 92px; letter-spacing: 0.5px;
  }

  .hero-art {
    position: absolute; left: 300px; top: 205px; width: 390px; height: 375px;
    background: radial-gradient(ellipse at 60% 55%, #f9c64a 0%, #fbe39a 35%, #fff6dc 60%, #ffffff 78%);
  }

  .testimonial {
    position: absolute; left: 30px; top: 328px; width: 330px;
    font-family: "Crimson Pro", serif; font-style: italic; font-weight: 300;
    font-size: 20px; line-height: 32px; color: var(--quote);
  }
  .testimonial .mark {
    font-family: Georgia, serif; font-style: normal; font-size: 44px; line-height: 0;
    color: #8a8a8a; position: relative;
  }
  .testimonial .open { display: block; height: 20px; top: 18px; }
  .testimonial p { padding-left: 21px; }
  .testimonial .close { top: 22px; left: 2px; }

  .intro {
    position: absolute; top: 612px; width: 370px;
    font-family: "Crimson Pro", serif; font-size: 23px; line-height: 28px; color: var(--ink);
  }
  .intro.left { left: 30px; }
  .intro.right { left: 447px; width: 395px; }

  .info-band {
    position: absolute; left: 0; top: 897px; width: 845px; height: 303px;
    background: linear-gradient(to bottom, var(--band-edge) 0px, #e0901c 5px, var(--band) 14px);
  }
  .band-heading {
    position: absolute; top: 929px;
    font-family: "Oswald", sans-serif; font-weight: 400; font-size: 14px;
    letter-spacing: 0.6px; color: var(--white); text-transform: uppercase;
  }
  .about-heading { left: 30px; }
  .booking-heading { left: 437px; }

  .about-text {
    position: absolute; left: 30px; top: 957px; width: 385px;
    font-family: "Crimson Pro", serif; font-size: 17.5px; line-height: 24px; color: var(--ink);
  }

  .contact { position: absolute; left: 437px; display: flex; align-items: center; }
  .contact.phone { top: 958px; }
  .contact.web { top: 1034px; }
  .contact svg { flex: none; }
  .phone-number {
    margin-left: 22px; font-family: "Crimson Pro", serif; font-weight: 700;
    font-size: 42px; color: var(--ink); letter-spacing: 0.5px;
  }
  .web-address {
    margin-left: 22px; font-family: "Crimson Pro", serif; font-weight: 700;
    font-size: 20px; line-height: 24px; color: var(--ink);
  }
</style>
</head>
<body>
<div class="flyer">
  <h1 class="title">Brain-based Strategies<br>for Student Success</h1>

  <div class="hero-art" role="img" aria-label="Yellow and red balloon animal shaped like a dog or giraffe, softly lit"></div>

  <blockquote class="testimonial">
    <span class="mark open">&ldquo;</span>
    <p>Dan was such an engaging and energetic presenter whom I enjoyed immensely.&nbsp; His presentation on the brain and take away strategies were so practical and meaningful. It was an invaluable session.<span class="mark close">&rdquo;</span></p>
  </blockquote>

  <p class="intro left">Contemporary teaching is a highly complex role as increasing numbers of students attend school without the essential ‘self-skills’ to be truly ‘school-ready’ and successful. Instead these students often seek-out attention in ways that can disruptive in the classroom causing stress and frustration for teachers.</p>

  <p class="intro right">Dan shows how and why the most effective strategies for these students are guided by a sound understanding of child-development and brain-development – especially where trauma has left lasting impacts. Teachers can learn how to build a student’s self-skills, without the teacher having to become a therapist!</p>

  <div class="info-band"></div>

  <h2 class="band-heading about-heading">About the presenter</h2>
  <p class="about-text">Daniel Whitford is a Melbourne-based therapist and educator with over twenty years experience working with adults and young people in the area of trauma and recovery. Dan’s seminars are engaging and practical since teachers need effective strategies that will immediately translate into classroom practice. Dan has trained here and overseas in the most effective behavior change strategies.</p>

  <h2 class="band-heading booking-heading">For more information or booking</h2>

  <div class="contact phone">
    <svg width="52" height="52" viewBox="0 0 52 52" aria-hidden="true">
      <circle cx="26" cy="26" r="23.5" fill="none" stroke="#111" stroke-width="3"/>
      <path d="M18.5 14.5c1.2-.8 2.3-.6 3 .5l2.6 4c.6 1 .4 2-.5 2.7l-1.6 1.2c.8 2.6 3.6 5.7 6.3 6.8l1.3-1.5c.8-.8 1.8-.9 2.7-.2l3.8 2.8c1 .8 1.1 1.9.3 3l-1.6 2c-1.3 1.5-3.6 1.9-6 .8-5.4-2.5-10-7.4-12-13-.8-2.4-.4-4.5 1-5.7z" fill="#111"/>
      <path d="M28 14.5a9.5 9.5 0 0 1 9.5 9.5M28 18.5a5.5 5.5 0 0 1 5.5 5.5" fill="none" stroke="#111" stroke-width="2" stroke-linecap="round"/>
    </svg>
    <span class="phone-number">0400 123 456</span>
  </div>

  <div class="contact web">
    <svg width="52" height="52" viewBox="0 0 52 52" aria-hidden="true">
      <circle cx="26" cy="26" r="23.5" fill="none" stroke="#111" stroke-width="3"/>
      <g fill="none" stroke="#111" stroke-width="2">
        <circle cx="26" cy="26" r="12"/>
        <ellipse cx="26" cy="26" rx="5.5" ry="12"/>
        <line x1="14" y1="26" x2="38" y2="26"/>
        <line x1="26" y1="14" x2="26" y2="38"/>
        <path d="M16 19.5h20M16 32.5h20"/>
      </g>
    </svg>
    <span class="web-address">www.danielwhitford.com.au/<br>studentsuccess</span>
  </div>
</div>
</body>
</html>
```